Business Cards and Stationary for Education Business with focus on social media
KiteHollow Education
Bright & Fun-filled
Mirela Dowsett
Managing Director
Unit 4/27
mirela.dowsett@kitehollowlearning.example
www.kitehollowlearning.example
KiteHollow Education runs seminars for parents and children to attend together aimed at online safety in the area of social media.
MirelaD MirelaD
Hi Designers, I have also decided to go with the logos rather than letter representations of Phone, E-mail etc. Could you please change these in the submissions you have left? Thank you Mirela
Hi Designers, Can whomever sees this first please replicate the #120 design for the front of a card in blue. I have written Pruv 3 messages and he hasn't replied so I am unsure if he is still active on this site. Warm Regards Mirela
Hi Designers, As mentioned in my initial comment I don't like green to dominate my cards. Also please submit a different front and back for each design. Warm Regards Mirela
Hi Designers, Thank you for your great submissions so far. Can I ask that you please submit back and front of business card each time. If it is 1 sided I will eliminate it as I would prefer to have the sides differ. I like use of blue and orange in block colour over green so please take this into consideration. I will give you all some individual feedback asap. Warm Regards Mirela

```html
<!DOCTYPE html>
<html lang="en">
<head>
<meta charset="utf-8">
<title>KiteHollow Education – Business Card</title>
<link href="https://fonts.googleapis.com/css2?family=Open+Sans:wght@400;600;700&display=swap" rel="stylesheet">
<style>
  :root{
    --bg:#e9e7e2;
    --sky:#29a3dd;
    --white:#ffffff;
    --orange:#f08a1c;
    --ink:#4a4a4a;
    --shadow:rgba(0,0,0,.22);
  }
  *{margin:0;padding:0;box-sizing:border-box}
  html,body{width:1200px;height:904px;overflow:hidden;background:var(--bg);font-family:"Open Sans",Arial,sans-serif}
  .canvas{position:relative;width:1200px;height:904px}
  .card{position:absolute;width:580px;height:330px;border-radius:22px;overflow:hidden;box-shadow:0 10px 26px var(--shadow)}
  .card--back{left:90px;top:90px;background:var(--sky)}
  .card--front{left:530px;top:480px;background:var(--white)}

  .card--back .illustration{position:absolute;left:70px;top:40px;width:200px;height:250px;border-radius:16px;
    background:linear-gradient(160deg,rgba(255,255,255,.35),rgba(255,255,255,.12))}
  .card--back .web{position:absolute;right:26px;bottom:56px;color:var(--white);font-size:10px;letter-spacing:.2px}

  .brand{position:absolute;left:28px;top:78px;display:flex;align-items:center;gap:8px;color:var(--orange);font-weight:700;font-size:26px;line-height:1.05;width:230px}
  .brand-mark{width:14px;height:14px;background:var(--orange);flex:none}
  .card--front .illustration{position:absolute;right:18px;top:36px;width:150px;height:220px;border-radius:14px;
    background:linear-gradient(160deg,#f6b25f 0%,#8cc8ea 55%,#29a3dd 100%);opacity:.85}
  .band{position:absolute;left:230px;right:0;top:150px;height:48px;background:var(--sky);color:var(--white);text-align:center;padding-top:6px}
  .band .name{font-weight:700;font-size:14px}
  .band .role{font-size:10.5px}
  .contacts{position:absolute;left:28px;top:226px;list-style:none;font-size:11px;color:var(--ink)}
  .contacts li{display:flex;align-items:center;gap:8px;height:17px;white-space:nowrap}
  .contacts svg{width:11px;height:11px;flex:none;fill:var(--orange)}
  .stripe{position:absolute;left:0;right:0;bottom:0;height:12px;background:var(--sky)}
</style>
</head>
<body>
<div class="canvas">
  <section class="card card--back">
    <div class="illustration" role="img" aria-label="Line illustration of a wifi signal with a parent and child inside a screen over a grid floor"></div>
    <p class="web">www.kitehollowlearning.example</p>
  </section>

  <section class="card card--front">
    <div class="brand"><span class="brand-mark"></span><span>KiteHollow Education</span></div>
    <div class="illustration" role="img" aria-label="Colourful illustration of a wifi signal with a parent and child beside a screen"></div>
    <div class="band">
      <p class="name">Mirela Dowsett</p>
      <p class="role">Managing Director</p>
    </div>
    <ul class="contacts">
      <li><svg viewBox="0 0 10 10"><path d="M5 0a3.5 3.5 0 0 0-3.5 3.5C1.5 6 5 10 5 10s3.5-4 3.5-6.5A3.5 3.5 0 0 0 5 0zm0 5a1.4 1.4 0 1 1 0-2.8A1.4 1.4 0 0 1 5 5z"/></svg>Unit 4/27</li>
      <li><svg viewBox="0 0 10 10"><path d="M2 0l2 2.4-1 1.2a6 6 0 0 0 3.4 3.4l1.2-1L10 8l-1.2 1.6C4.5 10 0 5.5.4 1.2z"/></svg>(07) 5550 1847</li>
      <li><svg viewBox="0 0 10 10"><path d="M0 2h10v6H0zM0 2l5 3.5L10 2" stroke="#fff" stroke-width=".8"/></svg>mirela.dowsett@kitehollowlearning.example</li>
      <li><svg viewBox="0 0 10 10"><circle cx="5" cy="5" r="4.5"/></svg>www.kitehollowlearning.example</li>
    </ul>
    <div class="stripe"></div>
  </section>
</div>
</body>
</html>
```